Billboard Design for Brightway Home Dentistry

Pinecrest Kinfolk Dental Care
Phone number: 318-572-0934
Address: 482 Coldbrook Blvd
Hours: 7am-5pm ; Monday-Friday

Dental Implant Surgery
Same Day Emergency Visits
Cosmetic Treatments
GLINT! Whitening

NAMES: Dr. Calvin Brastedder
Dr. Peter Haskell

MOST INSURANCES ACCEPTED

Eye catching slogan/colors/design for billboard

Our website is www.pinecrestkinfolkdentalcare.example to see current branding.

Target Market(s)

Target market is anyone in Alexandria. Focus on Families and High End Cosmetic Dentistry.

Industry/Entity Type

Dental Clinic

Requirements
Must have
• Pinecrest Kinfolk Dental Care
• Phone number: 318-572-0934
• Address: 482 Coldbrook Blvd
• Hours: 7am-5pm ; Monday-Friday
• Dental Implant Surgery
• Same Day Emergency Visits
• Cosmetic Treatments
• GLINT! Whitening
• NAMES: Dr. Calvin Brastedder
• Dr. Peter Haskell
• and logo
Nice to have
• digital billboard-try to catch attention with color or phrase
Should not have
• Can not make claims or compare to other area dentist's according to laws.

```html
<!DOCTYPE html>
<html lang="en">
<head>
<meta charset="utf-8">
<title>Pinecrest Kinfolk Dental Care – Billboard</title>
<link rel="stylesheet" href="https://fonts.googleapis.com/css2?family=Oswald:wght@300;400;500;600&family=Montserrat:wght@500;800&family=Roboto+Condensed:ital,wght@1,700&display=swap">
<style>
  :root {
    --navy: #0a0c8e;
    --navy-deep: #03046a;
    --sky: #3fd0f6;
    --sky-pale: #bff1ff;
    --white: #ffffff;
    --ink: #0b0f8f;
    --photo-top: #a9c6dc;
    --photo-bottom: #8f8273;
  }
  html, body {
    margin: 0;
    width: 1200px;
    height: 1200px;
    overflow: hidden;
    background: var(--white);
  }
  .billboard {
    position: absolute;
    left: 94px;
    top: 358px;
    width: 1013px;
    height: 482px;
    overflow: hidden;
    background: radial-gradient(ellipse at 60% 50%, #1216a6 0%, var(--navy) 45%, var(--navy-deep) 100%);
    font-family: "Oswald", sans-serif;
    color: var(--white);
  }
  .billboard-art {
    position: absolute;
    inset: 0;
  }
  .brand-name {
    position: absolute;
    left: 14px;
    top: 66px;
    width: 330px;
    margin: 0;
    text-align: center;
    font-family: "Montserrat", sans-serif;
    font-weight: 500;
    font-size: 23px;
    line-height: 1.15;
    letter-spacing: 1px;
    color: var(--sky);
    text-transform: uppercase;
  }
  .headline {
    position: absolute;
    left: 392px;
    width: 620px;
    margin: 0;
    text-align: center;
  }
  .headline-top {
    top: 16px;
    font-family: "Oswald", sans-serif;
    font-weight: 600;
    font-size: 58px;
    line-height: 1;
    letter-spacing: -0.5px;
  }
  .headline-main {
    top: 100px;
    font-family: "Montserrat", sans-serif;
    font-weight: 800;
    font-size: 58px;
    line-height: 1;
    background: linear-gradient(90deg, var(--sky) 0%, var(--sky-pale) 45%, var(--white) 60%, var(--sky) 90%);
    -webkit-background-clip: text;
    background-clip: text;
    color: transparent;
  }
  .services {
    position: absolute;
    margin: 0;
    padding: 0;
    list-style: none;
    font-weight: 500;
    font-size: 27px;
    line-height: 1;
  }
  .services li { position: absolute; white-space: nowrap; }
  .hours {
    position: absolute;
    left: 527px;
    top: 272px;
    display: flex;
    align-items: center;
    gap: 12px;
    font-family: "Roboto Condensed", sans-serif;
    font-style: italic;
    font-weight: 700;
    font-size: 27px;
    letter-spacing: 1.5px;
  }
  .doctor-band {
    position: absolute;
    left: 396px;
    top: 323px;
    width: 617px;
    height: 49px;
    background: linear-gradient(90deg, var(--sky) 0%, #d6f6ff 30%, var(--white) 45%, #d6f6ff 70%, var(--sky) 100%);
  }
  .doctor {
    position: absolute;
    top: 323px;
    height: 49px;
    line-height: 49px;
    font-weight: 400;
    font-size: 37px;
    color: var(--ink);
    white-space: nowrap;
    letter-spacing: -0.3px;
  }
  .doctor-divider {
    position: absolute;
    left: 740px;
    top: 332px;
    width: 2px;
    height: 32px;
    background: var(--ink);
  }
  .contact {
    position: absolute;
    top: 385px;
    display: flex;
    align-items: center;
    gap: 10px;
    font-family: "Roboto Condensed", sans-serif;
    font-style: italic;
    font-weight: 700;
    font-size: 27px;
    letter-spacing: 3px;
    white-space: nowrap;
  }
  .website {
    position: absolute;
    left: 392px;
    width: 620px;
    top: 444px;
    text-align: center;
    font-family: "Montserrat", sans-serif;
    font-weight: 800;
    font-size: 20px;
    letter-spacing: 3.4px;
  }
</style>
</head>
<body>
<main class="billboard">
  <svg class="billboard-art" width="1013" height="482" viewBox="0 0 1013 482">
    <defs>
      <linearGradient id="photo-tone" x1="0" y1="0" x2="0.3" y2="1">
        <stop offset="0" stop-color="var(--photo-top)"/>
        <stop offset="0.55" stop-color="#b59f88"/>
        <stop offset="1" stop-color="var(--photo-bottom)"/>
      </linearGradient>
      <linearGradient id="arc-tone" x1="0" y1="0" x2="0" y2="1">
        <stop offset="0" stop-color="var(--sky)"/>
        <stop offset="0.5" stop-color="var(--white)"/>
        <stop offset="1" stop-color="var(--sky)"/>
      </linearGradient>
      <clipPath id="photo-shape">
        <path d="M0,0 L282,0 Q554,242 250,482 L0,482 Z"/>
      </clipPath>
    </defs>
    <rect class="photo-area" x="0" y="140" width="460" height="342" fill="url(#photo-tone)" clip-path="url(#photo-shape)" role="img" aria-label="Photo of a smiling family: father, mother and young child outdoors"/>
    <path class="photo-arc" d="M282,0 Q554,242 250,482" fill="none" stroke="url(#arc-tone)" stroke-width="7"/>
  </svg>

  <p class="brand-name">Pinecrest Kinfolk<br>Dental Care</p>

  <h1 class="headline headline-top">Caring for all your family’s</h1>
  <h2 class="headline headline-main">DENTAL NEEDS</h2>

  <ul class="services">
    <li style="left:421px; top:183px;">•Dental Implant Surgery</li>
    <li style="left:701px; top:183px;">•Same Day Emergency Visits</li>
    <li style="left:421px; top:228px;">•Cosmetic Treatments</li>
    <li style="left:707px; top:228px;">•GLINT! Whitening</li>
  </ul>

  <div class="hours">
    <svg width="34" height="34" viewBox="0 0 34 34" aria-hidden="true">
      <circle cx="17" cy="17" r="14" fill="none" stroke="#fff" stroke-width="2.2"/>
      <path d="M17 9 V17 L23 20" fill="none" stroke="#fff" stroke-width="2.2" stroke-linecap="round"/>
    </svg>
    <span>7am-5pm ; Monday-Friday</span>
  </div>

  <div class="doctor-band"></div>
  <span class="doctor" style="left:432px;">Dr. Calvin Brastedder</span>
  <span class="doctor-divider"></span>
  <span class="doctor" style="left:764px;">Dr. Peter Haskell</span>

  <div class="contact" style="left:398px;">
    <svg width="32" height="32" viewBox="0 0 32 32" aria-hidden="true">
      <rect x="9" y="2" width="16" height="28" rx="3" fill="none" stroke="#fff" stroke-width="2.5"/>
      <path d="M3 10 Q1 16 3 22 L8 21 L8 11 Z" fill="#fff"/>
      <circle cx="17" cy="26" r="1.5" fill="#fff"/>
    </svg>
    <span>318-572-0934</span>
  </div>
  <div class="contact" style="left:690px;">
    <svg width="24" height="32" viewBox="0 0 24 32" aria-hidden="true">
      <path d="M12 2 C5 2 2 7 2 12 C2 19 12 30 12 30 C12 30 22 19 22 12 C22 7 19 2 12 2 Z" fill="#fff"/>
      <circle cx="12" cy="12" r="4.5" fill="var(--navy)"/>
    </svg>
    <span>482 Coldbrook Blvd</span>
  </div>

  <div class="website">www.pinecrestkinfolkdentalcare.example</div>
</main>
</body>
</html>
```